Onboarding Infographic/brochure

We are a small criminal defense firm looking to create some sort of infographic or brochure that we can onboard new clients with. We are currently sending it out via email but want something a bit cooler and fun to send to clients. The information is:

A Few Quick Rules

We are here to help each step of the way. While questions are never discouraged, this letter will answer some of the most common ones we get asked.

Communications

As a client, you should always be in the loop. While we will try to respond to questions as quickly as possible, sometimes we are unable to respond right away. Do not worry - we promise to get back to you soon. Some questions might take some time to research, and a correct answer is better than a quick one.

Appointments

One of the benefits of having an attorney is the ability to discuss your case outside of court, minus the stress and headaches. If you need an appointment, please contact the office.

Appointments must be scheduled in advance. We do not want you to make a special trip to the office only to learn that we are in court or otherwise unavailable.

Jail Visits

If your family member is currently in jail, we take that very seriously. We will visit your loved one and introduce ourselves. While the case is ongoing, we ask that a family member be designated a “contact” person so that messages can be relayed quickly. Never discuss the facts of the case over the phone with someone who is in jail. Jail calls are recorded and we have seen too many cases go south based on remarks made over recorded lines.

Police Reports and Discovery

We will do our best to provide you with copies of everything we receive on your case. Most information will be emailed, so please keep your email address up to date.

Changes in Contact Information

If you move or change numbers during the case, please let us know. It is difficult to help if we are unable to reach you, and helping you is why we are here.

Court Appearances

Cases do not get resolved as quickly as they do on television. Expect there to be several hearings in your case and it may be necessary for you to attend one or more of them. If a hearing is set, you will receive notice of the date and time of each hearing.

Billing and Collections

We understand that this investment was a huge decision for you. As we focus on providing the best representation, we will need for you to stay on schedule with any payment arrangements agreed to at the time of your initial consultation.

Again, thank you for your trust in us. We look forward to getting a fantastic outcome on your case.

Target Market(s)

Criminal defense clients and their families

Industry/Entity Type

Legal

Font styles to use
Serif

Requirements
Must have
• Must incorporate all of the rules we email out. Would like diagrams, images or pictures
Nice to have
• We attached a Welcome brochure. Not sure I want it to look super similar, hence the request for infographic.

```html
<!DOCTYPE html>
<html lang="en">
<head>
<meta charset="utf-8">
<title>A Few Quick Rules – Veritas Defense Group</title>
<link href="https://fonts.googleapis.com/css2?family=Montserrat:wght@800;900&family=Oswald:wght@600&family=Source+Serif+4:wght@300;400&display=swap" rel="stylesheet">
<style>
  :root {
    --ink: #000000;
    --panel-blue: #1479fb;
    --title-blue: #1690d9;
    --heading-navy: #0c1d4e;
    --white: #ffffff;
    --art-warm: #f6c244;
    --art-slate: #2f3a52;
    --art-grey: #dde1e7;
    --art-orange: #f2703d;
    --art-indigo: #3949a8;
    --art-skin: #f0c9a0;
  }
  * { box-sizing: border-box; margin: 0; padding: 0; }
  html, body { width: 816px; height: 1200px; overflow: hidden; background: var(--white); }
  body { position: relative; font-family: "Source Serif 4", Georgia, serif; color: var(--white); }

  .block { position: absolute; }
  .dark { background: var(--ink); }
  .panel { background: var(--panel-blue); text-align: center; }

  /* Header */
  .masthead { left: 22px; top: 20px; width: 773px; height: 196px; }
  .masthead__title {
    position: absolute; left: 34px; top: 30px;
    font-family: "Montserrat", sans-serif; font-weight: 900;
    font-size: 48px; line-height: 41px; letter-spacing: -2.5px;
    color: var(--title-blue); text-transform: uppercase;
  }
  .masthead__intro {
    position: absolute; left: 34px; top: 123px; width: 372px;
    font-size: 13.4px; line-height: 17.6px; font-weight: 400;
  }
  .brand {
    position: absolute; right: 34px; top: 64px; text-align: right;
    font-family: "Montserrat", sans-serif; font-weight: 800; color: var(--white);
    font-size: 30px; line-height: 33px; letter-spacing: 0.5px; text-transform: uppercase;
  }

  /* Panels */
  .panel__heading {
    position: absolute; left: 6px; right: 6px;
    font-family: "Oswald", sans-serif; font-weight: 600;
    font-size: 23px; line-height: 26px; color: var(--heading-navy);
    text-transform: uppercase; letter-spacing: -0.6px;
  }
  .panel__text {
    position: absolute;
    font-size: 12.4px; line-height: 15.9px; font-weight: 300;
  }
  .panel__text--tight { font-size: 11.6px; line-height: 14.5px; }
  .panel__art { position: absolute; border-radius: 14px; }

  .row-top { top: 225px; height: 377px; width: 252px; }
  .row-bottom { top: 706px; height: 327px; width: 252px; }
  .col-1 { left: 22px; }
  .col-2 { left: 282px; }
  .col-3 { left: 542px; }

  /* Billing band */
  .billing { left: 22px; top: 611px; width: 773px; height: 85px; }
  .billing__heading {
    position: absolute; left: 34px; top: 16px;
    font-family: "Oswald", sans-serif; font-weight: 600;
    font-size: 23px; line-height: 26px; letter-spacing: -0.6px; text-transform: uppercase;
  }
  .billing__text {
    position: absolute; left: 170px; top: 17px; width: 468px;
    font-size: 12.6px; line-height: 16px; font-weight: 300;
  }
  .billing__icon { position: absolute; left: 655px; top: 8px; width: 51px; height: 63px; }

  /* Closing */
  .closing { left: 21px; top: 1040px; width: 774px; height: 138px; }
  .closing__rule { position: absolute; height: 1px; background: #cfd3da; }
  .closing__mark {
    position: absolute; left: 365px; top: 23px; width: 45px; height: 27px;
    border-radius: 50%; background: radial-gradient(ellipse at center, var(--art-skin) 0 45%, #4a4f5a 75%);
  }
  .closing__text {
    position: absolute; left: 0; right: 0; top: 54px; text-align: center;
    font-size: 16.4px; line-height: 20px; font-weight: 300;
  }
</style>
</head>
<body>

  <header class="block dark masthead">
    <h1 class="masthead__title">A Few<br>Quick Rules</h1>
    <p class="masthead__intro">We are here to help each step of the way. While questions are never discouraged, this letter will answer some of the most common ones we get asked.</p>
    <div class="brand">Veritas<br>Defense Group</div>
  </header>

  <section class="block panel row-top col-1">
    <h2 class="panel__heading" style="top:27px">Appointments</h2>
    <p class="panel__text" style="top:55px;left:12px;right:12px">One of the benefits of having an attorney is the ability to discuss your case outside of court, minus the stress and headaches. If you need an appointment, please contact the office. Appointments must be scheduled in advance. We do not want you to make a special trip to the office only to learn that we are in court or otherwise unavailable.</p>
    <div class="panel__art" role="img" aria-label="Illustration of a hand holding a calendar page showing the 28th" style="left:0;top:229px;width:186px;height:126px;border-radius:0 12px 12px 0;background:linear-gradient(180deg,#f07a4a 0%,#f39a6e 20%,#f7f8fa 28%,#e9edf2 100%);"></div>
  </section>

  <section class="block panel row-top col-2">
    <div class="panel__art" role="img" aria-label="Illustration of two people talking with speech bubbles" style="left:44px;top:28px;width:154px;height:133px;background:linear-gradient(180deg,rgba(255,255,255,0.85) 0%,rgba(255,255,255,0.25) 38%,rgba(255,255,255,0) 45%),linear-gradient(90deg,var(--art-warm) 0%,#c9a567 48%,#4a4a66 55%,var(--art-slate) 100%);"></div>
    <h2 class="panel__heading" style="top:173px">Communications</h2>
    <p class="panel__text" style="top:201px;left:20px;right:22px">As a client, you should always be in the loop. While we will try to respond to questions as quickly as possible, sometimes we are unable to respond right away. Do not worry – we promise to get back to you soon. Some questions might take some time to research, and a correct answer is better than a quick one.</p>
  </section>

  <section class="block panel row-top col-3">
    <h2 class="panel__heading" style="top:18px">Jail Visits</h2>
    <p class="panel__text panel__text--tight" style="top:52px;left:14px;right:12px">If your family member is currently in jail, we take that very seriously. We will visit your loved one and introduce ourselves. While the case is ongoing, we ask that a family member be designated a “contact” person so that messages can be relayed quickly. Never discuss the facts of the case over the phone with someone who is in jail. Jail calls are recorded and we have seen too many cases go south based on remarks made over recorded lines.</p>
    <div class="panel__art" role="img" aria-label="Illustration of an attorney visiting an inmate at a table" style="left:65px;top:234px;width:114px;height:124px;background:linear-gradient(90deg,var(--art-slate) 0%,#3d4f8a 38%,#b07a66 55%,var(--art-orange) 80%);"></div>
  </section>

  <section class="block dark billing">
    <h2 class="billing__heading">Billing and<br>Collections</h2>
    <p class="billing__text">We understand that this investment was a huge decision for you. As we focus on providing the best representation, we will need for you to stay on schedule with any payment arrangements agreed to at the time of your initial consultation.</p>
    <svg class="billing__icon" viewBox="0 0 50 62" aria-hidden="true">
      <path d="M6 4 H44 V56 L40 60 L36 56 L32 60 L28 56 L24 60 L20 56 L16 60 L12 56 L8 60 L6 56 Z" fill="var(--art-indigo)"/>
      <rect x="13" y="12" width="24" height="2" fill="#fff"/>
      <rect x="13" y="20" width="24" height="2" fill="#fff"/>
      <rect x="13" y="28" width="24" height="2" fill="#fff"/>
      <rect x="13" y="36" width="16" height="2" fill="#fff"/>
      <text x="31" y="47" font-size="10" fill="#fff" font-family="Source Serif 4, serif">$</text>
    </svg>
  </section>

  <section class="block panel row-bottom col-1">
    <h2 class="panel__heading" style="top:27px">Court Appearances</h2>
    <p class="panel__text" style="top:56px;left:18px;right:22px">Cases do not get resolved as quickly as they do on television. Expect there to be several hearings in your case and it may be necessary for you to attend one or more of them. If a hearing is set, you will receive notice of the date and time of each hearing.</p>
    <div class="panel__art" role="img" aria-label="Illustration of a judge with a gavel" style="left:61px;top:200px;width:123px;height:118px;border-radius:40% 40% 10px 10px;background:linear-gradient(180deg,#eef0f4 0%,#d5d9e0 40%,#3a4150 58%,var(--art-slate) 100%);"></div>
  </section>

  <section class="block panel row-bottom col-2">
    <div class="panel__art" role="img" aria-label="Illustration of documents under a magnifying glass" style="left:68px;top:26px;width:98px;height:126px;background:radial-gradient(circle at 38% 55%,#f4f6f8 0 30%,#56606e 31% 37%,rgba(0,0,0,0) 38%),linear-gradient(135deg,#eef1f4,#c3c9d2);"></div>
    <h2 class="panel__heading" style="top:164px">Changes in Contact<br>Information</h2>
    <p class="panel__text" style="top:221px;left:18px;right:16px">If you move or change numbers during the case, please let us know. It is difficult to help if we are unable to reach you, and helping you is why we are here.</p>
  </section>

  <section class="block panel row-bottom col-3">
    <h2 class="panel__heading" style="top:28px">Police Reports and<br>Discovery</h2>
    <p class="panel__text" style="top:82px;left:24px;right:22px">We will do our best to provide you with copies of everything we receive on your case. Most information will be emailed, so please keep your email address up to date.</p>
    <div class="panel__art" role="img" aria-label="Illustration of hands signing a police report on a clipboard" style="left:57px;top:182px;width:133px;height:144px;border-radius:10px 10px 0 0;background:linear-gradient(180deg,#f2cf45 0%,#f2cf45 9%,#f6f7f9 14%,#e6e9ee 62%,var(--art-skin) 72%,var(--art-slate) 90%);"></div>
  </section>

  <footer class="block dark closing">
    <span class="closing__rule" style="left:246px;top:36px;width:94px"></span>
    <div class="closing__mark" role="img" aria-label="Handshake icon"></div>
    <span class="closing__rule" style="left:430px;top:36px;width:94px"></span>
    <p class="closing__text">Again, thank you for your trust in us.<br>We look forward to getting a fantastic outcome on your case.</p>
    <span class="closing__rule" style="left:245px;top:107px;width:281px"></span>
  </footer>

</body>
</html>
```